Web Design Project for Web Agency

WHAT I NEED:
The design I need (PSD file) is for a microsite designed for employee recruitment for Brantley, a Web agency.
***Design for the 1st Page ONLY : "Manifeste"
OBJECTIVES OF THE WEBSITE:
1. To promote the agency's corporate culture and HR management principles.
2. To get people to apply on available jobs
ELEMENTS OF THE PAGE "MANIFESTE" :
1. Brantley logo (see attached files). Beside the logo must be the word "Carrières" ("Careers" in english)
***The logo is not final and there is NO branding for Brantley yet. That is why there are multiple files. So please feel free to be creative!
2. Main menu : 4 sections
Manifeste | Opportunités | Brantly | Postuler
3. Manifeste :
This page is the home page. It will present 2 main sections :
a. The agency's corporate culture :
- Title of the page is a question : "Do you embrace Brantley's corporate culture?"
- Then, presentation of the 5 corporate values, each with a title and short description
- At the end of the list of values, we want a button that says "Apply now"
b. The agency's HR management principles :
- Title of the page is a question : "Do you see yourself working at Brantley?"
- Then, presentation of the 5 Management principles, each with a title and short description
- At the end of the list of principles, we want a button that says "Apply now"
VISUAL INSPIRATION
To create each section of the "Manifeste" page, we want a design that will fit with the corporate culture:
- Brantley is BOLD
- Brantley is PROUD
- Brantley is PROFESSIONAL
- Brantley is ELEGANT
- Brantley is REFINED
We want something slick and modern. Here are some Website's that we like that can be of inspiration:
- http://www.studio-vetrak.com/en/services
- http://quorvinpanels.com/

```html
<!DOCTYPE html>
<html lang="en">
<head>
<meta charset="utf-8">
<title>Brantley – Carrières – Manifeste</title>
<link rel="stylesheet" href="https://fonts.googleapis.com/css2?family=Josefin+Sans:wght@400;600;700&family=Arimo:wght@400&display=swap">
<style>
:root{
  --orange:#f47a3a;
  --orange-dark:#e0662a;
  --teal:#3ec3c5;
  --teal-dark:#1f9fa3;
  --ink:#1c1c1c;
  --header:#151515;
  --footer:#1e1e1e;
  --footer-bar:#141414;
  --line:#e2e2e2;
  --muted:#9a9a9a;
  --card-border:#dcdcdc;
  --white:#ffffff;
}
*{box-sizing:border-box;margin:0;padding:0}
html,body{width:908px;height:1200px;overflow:hidden;background:var(--white)}
body{position:relative;font-family:"Josefin Sans",sans-serif;color:var(--ink)}
.abs{position:absolute}

/* header */
.site-header{position:absolute;left:0;top:0;width:908px;height:51px;background:linear-gradient(#262626,var(--header));border-bottom:2px solid var(--orange)}
.brand{position:absolute;left:141px;top:8px;color:var(--orange);font-weight:700;font-size:25px;letter-spacing:0.5px}
.brand-sub{position:absolute;left:147px;top:36px;color:#bbb;font-size:6.5px;letter-spacing:2.4px}
.main-nav{position:absolute;left:323px;top:0;height:49px;display:flex;align-items:center;font-size:11.5px;color:#ddd}
.main-nav a{color:#ddd;text-decoration:none;padding:0 12px}
.main-nav .sep{color:#999}
.main-nav .active{background:#2c2c2c;color:var(--orange);height:49px;line-height:52px;padding:0 14px;position:relative}
.main-nav .active::after{content:"";position:absolute;left:50%;bottom:0;margin-left:-4px;border:4px solid transparent;border-bottom-color:var(--orange)}
.btn{position:absolute;display:flex;align-items:center;background:linear-gradient(#7ad9db,var(--teal) 45%,var(--teal-dark));border-radius:2px;color:#0f4f52;font-size:13px;text-decoration:none;border:1px solid #2aa8ab}
.btn .label{flex:1;text-align:center;padding-top:3px}
.btn .go{width:34px;height:100%;border-left:1px solid #2a9da0;display:flex;align-items:center;justify-content:center}
.btn .go i{width:14px;height:14px;border-radius:50%;background:#145d60;position:relative}
.btn .go i::after{content:"";position:absolute;left:5px;top:3.5px;border-left:5px solid var(--teal);border-top:3.5px solid transparent;border-bottom:3.5px solid transparent}

/* hero */
.hero{position:absolute;left:0;top:51px;width:908px;height:431px;background:linear-gradient(100deg,#6a4a36 0%,#c9a88c 30%,#efe7df 50%,#b28f74 72%,#5e4a3f 100%)}
.hero-caption{position:absolute;left:189px;top:201px;width:526px;height:59px;background:rgba(110,100,95,.55);color:var(--white);text-align:center;font-size:12px;padding-top:9px;line-height:19px}
.hero-caption strong{font-weight:400;font-size:19px}
.slider-dots{position:absolute;top:493px;left:431px;display:flex;gap:3px}
.slider-dots i{width:9px;height:9px;border-radius:50%;border:1px solid #bbb}
.slider-dots i.on{background:radial-gradient(#bbb 35%,transparent 40%)}

/* sections */
.divider{position:absolute;left:351px;width:206px;height:14px}
.section-title{position:absolute;left:0;width:908px;text-align:center;color:var(--orange);font-size:17px;letter-spacing:.4px}
.card{position:absolute;width:166px;height:115px;border:1px solid var(--card-border);background:var(--white);text-align:center}
.card h3{font-size:10.5px;font-weight:600;margin-top:32px;color:#222}
.card p{font-family:Arimo,sans-serif;font-size:7px;line-height:11px;color:var(--muted);margin:14px 7px 0}
.card.is-featured{background:var(--orange);border-color:var(--orange)}
.card.is-featured h3,.card.is-featured p{color:var(--white)}
.badge{position:absolute;width:58px;height:58px;border-radius:50%;background:var(--white);border:2px solid var(--orange);box-shadow:0 0 0 3px #f3f3f3;display:flex;align-items:center;justify-content:center}
.badge.is-filled{background:var(--orange)}
.arrow{position:absolute;width:12px;height:24px}

/* footer */
.tweets{position:absolute;left:0;top:1073px;width:908px;height:88px;background:var(--footer);color:var(--white);text-align:center}
.tweets-head{position:absolute;left:0;top:14px;width:908px;display:flex;justify-content:center;align-items:center;gap:8px;color:var(--orange);font-size:13px}
.tweets-head i{width:16px;height:16px;border-radius:50%;background:var(--orange)}
.tweet{position:absolute;left:0;top:47px;width:908px;font-size:11px}
.tweet em{font-style:normal;color:var(--orange)}
.media{position:absolute;left:0;top:66px;width:908px;font-size:11px;display:flex;justify-content:center;align-items:center;gap:7px}
.media i{width:11px;height:8px;background:var(--teal)}
.footer-bar{position:absolute;left:0;top:1161px;width:908px;height:39px;background:var(--footer-bar)}
.copyright{position:absolute;left:141px;top:15px;font-family:Arimo,sans-serif;font-size:7px;color:#aaa}
.copyright b{color:var(--orange)}
.social{position:absolute;left:703px;top:10px;display:flex;gap:4px}
.social i{width:18px;height:18px;border-radius:50%;border:1.5px solid #ddd}
</style>
</head>
<body>

<header class="site-header">
  <div class="brand">Brantley</div>
  <div class="brand-sub">AGENCE NUMÉRIQUE</div>
  <nav class="main-nav">
    <a class="active" href="#">Manifeste</a>
    <a href="#">Opportunités</a><span class="sep">|</span>
    <a href="#">Brantly</a><span class="sep">|</span>
    <a href="#">Postuler</a>
  </nav>
  <a class="btn" href="#" style="left:634px;top:12px;width:131px;height:25px"><span class="label">Careers</span><span class="go"><i></i></span></a>
</header>

<section class="hero" role="img" aria-label="Photo of four business professionals in suits reviewing documents and folders together in an office">
  <div class="hero-caption"><strong>Sed hendrerit arcu</strong> vel vulputate vestibulum. Curabitur hendrerit tortor quis nisi<br>imperdiet vitae tempus sapien egestas. Donec commodo est quis urna euismod mollis.</div>
</section>
<div class="slider-dots"><i class="on"></i><i></i><i></i><i></i></div>

<svg class="divider" style="top:510px" viewBox="0 0 206 14"><line x1="0" y1="8" x2="90" y2="8" stroke="#e2e2e2"/><line x1="116" y1="8" x2="206" y2="8" stroke="#e2e2e2"/><path d="M104 1 L99 8 H103 L101 13 L107 6 H103 Z" fill="#c5ccd3"/></svg>

<!-- corporate culture -->
<h2 class="section-title" style="top:536px">Do you embrace Brantley's corporate culture?</h2>
<svg class="arrow" style="left:140px;top:665px" viewBox="0 0 12 24"><path d="M11 1 L1 12 L11 23" fill="none" stroke="#ccc" stroke-width="1.5"/></svg>
<svg class="arrow" style="left:754px;top:665px" viewBox="0 0 12 24"><path d="M1 1 L11 12 L1 23" fill="none" stroke="#ccc" stroke-width="1.5"/></svg>

<article class="card" style="left:178px;top:605px"><h3>Pellentesque viverra</h3><p>Lorem ipsum dolor sit amet, consectetur adipiscing elit. Ut sit amet pretium sapien, vel placerat orci Cras rutrum nisi , convallis erat ultrices. Vivamus congue.</p></article>
<article class="card is-featured" style="left:370px;top:605px"><h3>Sed tempus euismod nisi</h3><p>Lorem ipsum dolor sit amet, consectetur adipiscing elit. Ut sit amet pretium sapien, vel placerat orci Cras rutrum nisi , convallis erat ultrices. Vivamus congue.</p></article>
<article class="card" style="left:563px;top:605px"><h3>Donec ac ipsum augue</h3><p>Lorem ipsum dolor sit amet, consectetur adipiscing elit. Ut sit amet pretium sapien, vel placerat orci Cras rutrum nisi , convallis erat ultrices. Vivamus congue.</p></article>

<div class="badge" style="left:232px;top:564px"><svg width="26" height="22" viewBox="0 0 26 22"><rect x="1" y="6" width="24" height="15" fill="none" stroke="#f47a3a" stroke-width="1.6"/><path d="M1 6 L13 15 L25 6" fill="none" stroke="#f47a3a" stroke-width="1.6"/><circle cx="13" cy="5" r="4" fill="#fff" stroke="#f47a3a" stroke-width="1.6"/></svg></div>
<div class="badge is-filled" style="left:424px;top:564px"><svg width="24" height="22" viewBox="0 0 24 22"><path d="M9 1 H15 V9 H19 L12 16 L5 9 H9 Z" fill="#fff"/><path d="M1 14 V21 H23 V14" fill="none" stroke="#fff" stroke-width="2"/></svg></div>
<div class="badge" style="left:617px;top:564px"><svg width="24" height="24" viewBox="0 0 24 24"><path d="M4 20 L6 14 L17 3 L21 7 L10 18 Z" fill="none" stroke="#f47a3a" stroke-width="1.8"/><line x1="3" y1="22" x2="21" y2="22" stroke="#f47a3a" stroke-width="1.8"/></svg></div>

<a class="btn" href="#" style="left:369px;top:741px;width:167px;height:26px"><span class="label">Apply Now</span><span class="go"><i></i></span></a>

<svg class="divider" style="top:778px" viewBox="0 0 206 14"><line x1="0" y1="8" x2="90" y2="8" stroke="#e2e2e2"/><line x1="116" y1="8" x2="206" y2="8" stroke="#e2e2e2"/><path d="M104 1 L99 8 H103 L101 13 L107 6 H103 Z" fill="#c5ccd3"/></svg>

<!-- HR principles -->
<h2 class="section-title" style="top:805px">Do you see yourself working at Brantley?</h2>
<svg class="arrow" style="left:140px;top:934px" viewBox="0 0 12 24"><path d="M11 1 L1 12 L11 23" fill="none" stroke="#ccc" stroke-width="1.5"/></svg>
<svg class="arrow" style="left:754px;top:934px" viewBox="0 0 12 24"><path d="M1 1 L11 12 L1 23" fill="none" stroke="#ccc" stroke-width="1.5"/></svg>

<article class="card" style="left:178px;top:877px"><h3>Pellentesque viverra</h3><p>Lorem ipsum dolor sit amet, consectetur adipiscing elit. Ut sit amet pretium sapien, vel placerat orci Cras rutrum nisi , convallis erat ultrices. Vivamus congue.</p></article>
<article class="card" style="left:370px;top:877px"><h3>Sed tempus euismod nisi</h3><p>Lorem ipsum dolor sit amet, consectetur adipiscing elit. Ut sit amet pretium sapien, vel placerat orci Cras rutrum nisi , convallis erat ultrices. Vivamus congue.</p></article>
<article class="card" style="left:563px;top:877px"><h3>Donec ac ipsum augue</h3><p>Lorem ipsum dolor sit amet, consectetur adipiscing elit. Ut sit amet pretium sapien, vel placerat orci Cras rutrum nisi , convallis erat ultrices. Vivamus congue.</p></article>

<div class="badge" style="left:232px;top:835px"><svg width="26" height="22" viewBox="0 0 26 22"><rect x="1" y="6" width="24" height="15" fill="none" stroke="#f47a3a" stroke-width="1.6"/><path d="M1 6 L13 15 L25 6" fill="none" stroke="#f47a3a" stroke-width="1.6"/><circle cx="13" cy="5" r="4" fill="#fff" stroke="#f47a3a" stroke-width="1.6"/></svg></div>
<div class="badge" style="left:424px;top:835px"><svg width="24" height="22" viewBox="0 0 24 22"><path d="M9 1 H15 V9 H19 L12 16 L5 9 H9 Z" fill="#f47a3a"/><path d="M1 14 V21 H23 V14" fill="none" stroke="#f47a3a" stroke-width="2"/></svg></div>
<div class="badge" style="left:617px;top:835px"><svg width="24" height="24" viewBox="0 0 24 24"><path d="M4 20 L6 14 L17 3 L21 7 L10 18 Z" fill="none" stroke="#f47a3a" stroke-width="1.8"/><line x1="3" y1="22" x2="21" y2="22" stroke="#f47a3a" stroke-width="1.8"/></svg></div>

<a class="btn" href="#" style="left:369px;top:1007px;width:167px;height:26px"><span class="label">Apply Now</span><span class="go"><i></i></span></a>

<svg class="divider" style="top:1045px" viewBox="0 0 206 14"><line x1="0" y1="8" x2="90" y2="8" stroke="#e2e2e2"/><line x1="116" y1="8" x2="206" y2="8" stroke="#e2e2e2"/><path d="M104 1 L99 8 H103 L101 13 L107 6 H103 Z" fill="#c5ccd3"/></svg>

<!-- footer -->
<footer>
  <section class="tweets">
    <div class="tweets-head"><i></i>Tweets</div>
    <p class="tweet"><em>Brantley</em> @sollicitudin arcu &nbsp;<em>rutrum diam.</em> Nullam congue nisi vel dui vulputate pellentesque.</p>
    <p class="media"><i></i>View media</p>
  </section>
  <div class="footer-bar">
    <p class="copyright">Copyright © 2013 <b>Brantley</b></p>
    <div class="social"><i></i><i></i><i></i></div>
  </div>
</footer>

</body>
</html>
```